Existing WP site needs a fresh look (design only)

The current website, www.quorrahub.com.au, is fine, but needs a fresh look so their clients can tell their website has been 'refreshed' regularly.
https://www.quorrahub.com.au/sitemap/
They will use the existing functionality.
They want to keep the blue, green and white of their logo as the main colors, but a fresh look. They prefer a light look to a dark look, but they would be open to good designs that change their mind.
Be creative, think outside the box.
You only need to supply the 'home page ' design to win but the winners will be asked to provide an extra 'standard' page template (like the one currently being used for search results and other pages)
Any photos used must be supplied without charge with the PSDs in a resolution acceptable for the WordPress site.

```html
<!DOCTYPE html>
<html lang="en">
<head>
<meta charset="utf-8">
<title>Quorra Hub – Professional Voice Casting</title>
<link href="https://fonts.googleapis.com/css2?family=Exo+2:wght@300;400;600;700;800&family=Raleway:ital,wght@0,400;0,500;0,600;0,700;1,400&display=swap" rel="stylesheet">
<style>
:root{
  --green:#7cc142;
  --green-dark:#5fa02c;
  --navy:#1b2b40;
  --navy-deep:#14202f;
  --ink:#1c2c44;
  --muted:#6b7684;
  --ghost:#dfe4ea;
  --white:#ffffff;
  --line:#e6e9ee;
}
*{box-sizing:border-box;margin:0;padding:0}
html,body{width:1200px;height:4422px;overflow:hidden}
body{position:relative;font-family:"Raleway",sans-serif;color:var(--ink);background:var(--white)}
.section{position:absolute;left:0;width:1200px;overflow:hidden}
.abs{position:absolute}
h2,h3,.brand,.btn{font-family:"Exo 2",sans-serif}

/* header + hero */
.hero{top:0;height:695px;background:var(--navy-deep)}
.hero-photo{position:absolute;inset:0;background:radial-gradient(ellipse 420px 300px at 760px 200px,#56606c 0%,#2c3744 45%,#18222f 80%),linear-gradient(#1d2836,#14202f)}
.hero-wave{position:absolute;left:0;right:0;top:420px;height:280px;background:radial-gradient(ellipse 500px 120px at 250px 160px,rgba(124,193,66,.35),transparent 70%),radial-gradient(ellipse 520px 110px at 1000px 120px,rgba(124,193,66,.3),transparent 70%)}
.topbar{position:absolute;left:0;right:0;top:0;height:92px;border-bottom:1px solid rgba(255,255,255,.08)}
.phone{position:absolute;top:16px;display:flex;align-items:center;gap:8px;color:var(--white);font-size:13px;font-weight:500}
.phone svg{width:20px;height:20px}
.nav{position:absolute;top:58px;display:flex;gap:48px;font-size:12px;font-weight:500;color:var(--white);text-transform:uppercase}
.nav .active{color:var(--green);position:relative}
.nav .active::after{content:"";position:absolute;left:-2px;right:-12px;top:24px;height:2px;background:var(--green)}
.brand{position:absolute;left:525px;top:14px;width:150px;text-align:center;color:var(--white);font-weight:700;font-size:24px;line-height:1;display:flex;align-items:center;gap:8px;justify-content:center}
.brand i{display:block;width:12px;height:12px;background:var(--green)}
.ghost{position:absolute;left:0;right:0;text-align:center;font-family:"Exo 2",sans-serif;font-weight:400;color:transparent;-webkit-text-stroke:1.5px var(--ghost);letter-spacing:10px;white-space:nowrap}
.hero .ghost{top:185px;font-size:110px;-webkit-text-stroke:2px rgba(124,193,66,.55)}
.hero-title{position:absolute;left:0;right:0;top:258px;text-align:center;color:var(--white);font-family:"Exo 2",sans-serif;font-weight:800;font-size:54px;letter-spacing:5px}
.hero-sub{position:absolute;left:0;right:0;top:316px;text-align:center;color:var(--white);font-family:"Raleway",sans-serif;font-weight:500;font-size:40px;letter-spacing:7px}
.search{position:absolute;left:342px;top:386px;width:527px;height:54px;background:var(--white);display:flex}
.search span{flex:1;padding:19px 20px;font-size:12px;font-weight:700;color:var(--ink)}
.search b{width:54px;background:var(--green);display:flex;align-items:center;justify-content:center}
.chev{position:absolute;left:584px;top:488px}

/* filter panel */
.filter{position:absolute;left:209px;top:597px;width:765px;height:145px;background:var(--green);z-index:2}
.select{position:absolute;width:234px;height:32px;background:var(--white);font-size:9px;font-weight:600;padding:12px 14px;text-transform:uppercase;color:var(--ink)}
.select::after{content:"";position:absolute;right:14px;top:11px;width:6px;height:6px;border-right:1.5px solid var(--ink);border-bottom:1.5px solid var(--ink);transform:rotate(45deg)}
.submit{position:absolute;left:515px;top:720px;width:148px;height:36px;border-radius:18px;background:var(--navy);color:var(--white);font:600 12px "Raleway",sans-serif;display:flex;align-items:center;justify-content:center;z-index:3}

/* titles */
.sec-title{position:absolute;left:0;right:0;text-align:center;font-size:34px;font-weight:700;letter-spacing:.5px;text-transform:uppercase}
.sec-title .light{font-weight:400}
.sec-title::after{content:"";display:block;width:56px;height:3px;background:var(--green);margin:8px auto 0}
.btn{position:absolute;display:flex;align-items:center;justify-content:center;border-radius:22px;background:var(--green);color:var(--white);font-weight:700;font-size:13px;text-transform:uppercase}

/* spotlight */
.spotlight{top:695px;height:684px;background:linear-gradient(#f6f8fb,#ffffff 60%)}
.spot-glow{position:absolute;inset:0;background:radial-gradient(ellipse 260px 120px at 950px 170px,rgba(124,193,66,.25),transparent 70%),radial-gradient(ellipse 200px 260px at 40px 460px,rgba(120,90,220,.25),transparent 70%)}
.spotlight .ghost{top:105px;font-size:86px}
.spotlight .sec-title{top:150px}
.card{position:absolute;top:251px;width:211px;height:309px;background:var(--white);border:1.5px solid #cfe5bb;border-radius:4px;overflow:hidden;text-align:center}
.card .photo{height:194px;background:linear-gradient(160deg,#5f6e7c,#2e3a46)}
.card h3{margin-top:18px;font-size:15px;font-weight:700;color:var(--ink);text-transform:uppercase}
.card .role{font-size:12px;color:var(--muted);margin-top:4px}
.card p{font-size:11px;line-height:1.5;color:var(--muted);margin:6px 18px 0}
.card.featured{background:var(--green);border-color:var(--green)}
.card.featured h3,.card.featured .role,.card.featured p{color:var(--white)}
.arrow{position:absolute;width:22px;height:22px;border-left:2px solid #9aa3ad;border-bottom:2px solid #9aa3ad}
.arrow.left{transform:rotate(45deg)}
.arrow.right{transform:rotate(-135deg)}

/* about */
.about{top:1379px;height:595px;background:var(--navy)}
.about-wave{position:absolute;inset:0;background:radial-gradient(ellipse 600px 130px at 500px 520px,rgba(40,180,160,.4),transparent 70%),radial-gradient(ellipse 400px 90px at 150px 480px,rgba(124,193,66,.25),transparent 70%)}
.about .ghost{left:138px;right:auto;top:78px;font-size:64px;-webkit-text-stroke:1.5px rgba(255,255,255,.12);letter-spacing:6px}
.about h2{position:absolute;left:144px;top:110px;font-size:36px;font-weight:700;color:var(--white)}
.about p{position:absolute;left:142px;width:410px;font-size:14.5px;line-height:1.6;color:#d7dde5}
.ring{position:absolute;border-radius:50%;border:1.5px solid rgba(124,193,66,.55)}
.about-photo{position:absolute;left:689px;top:72px;width:388px;height:388px;border-radius:50%;background:radial-gradient(circle at 60% 45%,#3b3f44,#1a1d22 55%),#222;overflow:hidden}
.about-photo::after{content:"";position:absolute;inset:0;background:radial-gradient(circle at 20% 40%,rgba(230,150,60,.55),transparent 45%),radial-gradient(circle at 85% 30%,rgba(90,160,220,.45),transparent 45%)}

/* news */
.news{top:1974px;height:662px;background:linear-gradient(#f4f6f9,#ffffff 50%)}
.news .ghost{top:60px;font-size:86px}
.news .sec-title{top:100px}
.news-main{position:absolute;left:153px;top:193px;width:462px;height:383px;background:var(--white);border:1px solid var(--line)}
.news-main .photo{height:249px;background:linear-gradient(135deg,#2a2a2e,#8a6d2c 55%,#1f1f22)}
.news-main h3{margin:16px 0 0 28px;font-size:16px;font-weight:700;color:var(--ink);text-transform:uppercase}
.news-main p{margin:8px 28px 0;font-size:12px;line-height:1.5;color:var(--muted)}
.news-side{position:absolute;left:630px;width:462px;height:186px;background:var(--white);border:1.5px solid #cfe5bb}
.news-side .photo{position:absolute;left:0;top:0;width:213px;height:100%}
.news-side .txt{position:absolute;left:235px;top:30px;width:210px}
.news-side h3{font-size:15px;font-weight:700;color:var(--ink);text-transform:uppercase}
.news-side .by{font-size:13px;color:var(--ink);margin-top:4px}
.news-side p{font-size:10.5px;line-height:1.6;color:var(--muted);margin-top:8px}
.wave-band{position:absolute;left:0;right:0;top:2627px;height:70px;background:linear-gradient(90deg,rgba(28,44,68,.7),rgba(124,193,66,.8) 50%,rgba(28,44,68,.7));-webkit-mask:linear-gradient(transparent 20%,#000 45%,#000 55%,transparent 80%);mask:linear-gradient(transparent 20%,#000 45%,#000 55%,transparent 80%)}

/* reviews */
.reviews{top:2680px;height:737px;background:linear-gradient(#1c2c44,#17253a)}
.reviews-wave{position:absolute;inset:0;background:radial-gradient(ellipse 700px 120px at 600px 620px,rgba(40,170,200,.35),transparent 70%),radial-gradient(ellipse 400px 90px at 200px 600px,rgba(124,193,66,.3),transparent 70%),radial-gradient(ellipse 300px 90px at 1050px 640px,rgba(110,80,220,.35),transparent 70%)}
.reviews .ghost{top:96px;font-size:86px;-webkit-text-stroke:1.5px rgba(255,255,255,.1)}
.reviews .sec-title{top:130px;color:var(--white)}
.bubble{position:absolute;border-radius:50%;background:#203249;text-align:center;color:#8893a2}
.bubble .q{font-family:"Exo 2",sans-serif;font-size:96px;font-weight:800;line-height:1;height:60px;color:#3a4b60}
.bubble p{font-style:italic;font-size:10.5px;line-height:1.8;margin:0 40px}
.bubble .who{margin-top:18px;font-size:14px;color:#aab3bf}
.bubble .loc{font-size:10px;margin-top:4px}
.bubble.main{background:var(--green);color:var(--white);box-shadow:0 0 0 10px rgba(124,193,66,.25)}
.bubble.main .q{color:var(--white)}
.bubble.main p{font-size:13.5px;margin:0 48px}
.cite{display:flex;align-items:center;justify-content:center;gap:10px;margin-top:18px}
.cite i{width:42px;height:42px;border-radius:50%;background:var(--white)}
.cite b{display:block;font-size:13px;text-align:left}
.cite small{display:block;font-size:10px;text-align:left;margin-top:3px}

/* clients */
.clients{top:3417px;height:592px;background:linear-gradient(#f5f7fa,#ffffff 40%)}
.clients .ghost{top:70px;font-size:86px}
.clients .sec-title{top:112px}
.clients .sec-title em{font-style:normal;color:var(--green)}
.client{position:absolute;width:170px;text-align:center;font-family:"Raleway",sans-serif;font-weight:700;font-size:17px;color:#a7adb5}
.client-box{position:absolute;left:266px;top:249px;width:175px;height:82px;border:1.5px solid #cfe5bb;background:var(--white);box-shadow:0 6px 20px rgba(124,193,66,.25)}
.dots{position:absolute;top:508px;left:538px;display:flex;gap:12px}
.dots i{width:36px;height:3px;background:#e3e6ea}
.dots i:first-child{background:var(--green)}

/* footer */
.footer{top:4009px;height:413px;background:var(--navy)}
.footer-wave{position:absolute;inset:0;background:radial-gradient(ellipse 260px 90px at 160px 170px,rgba(124,193,66,.18),transparent 70%)}
.footer .brand{left:125px;top:100px;width:auto;font-size:30px;justify-content:flex-start}
.footer .tag{position:absolute;left:127px;top:146px;color:var(--white);font-weight:700;font-size:13px;letter-spacing:1px}
.fcol{position:absolute;top:96px;color:var(--white)}
.fcol h4{font-family:"Raleway",sans-serif;font-weight:500;font-size:16px;text-transform:uppercase;padding-bottom:8px;border-bottom:1px solid rgba(255,255,255,.25);margin-bottom:14px;display:inline-block}
.fcol li{list-style:none;font-size:12px;color:#c9d0d9;line-height:27px}
.contact-row{display:flex;gap:12px;font-size:12px;line-height:24px;color:#c9d0d9;margin-bottom:6px}
.contact-row svg{flex:none;margin-top:4px}
.copy{position:absolute;left:0;right:0;top:4385px;text-align:center;font-size:11px;color:#7f8a98}
</style>
</head>
<body>

<!-- HERO -->
<section class="section hero">
  <div class="hero-photo" role="img" aria-label="Studio condenser microphone in a dim recording booth"></div>
  <div class="hero-wave" role="img" aria-label="Flowing green sound-wave particles"></div>
  <header class="topbar">
    <div class="phone" style="left:113px">
      <svg viewBox="0 0 20 20"><circle cx="10" cy="10" r="10" fill="#7cc142"/><path d="M7 5.5l1.6 2.4-1 1.2a6 6 0 003 3l1.2-1 2.4 1.6-.8 1.7c-3.9.2-7.6-3.5-7.4-7.4z" fill="#fff"/></svg>
      MELBOURNE:+ 61 3 9000 1234
    </div>
    <div class="phone" style="left:855px">
      <svg viewBox="0 0 20 20"><circle cx="10" cy="10" r="10" fill="#7cc142"/><path d="M7 5.5l1.6 2.4-1 1.2a6 6 0 003 3l1.2-1 2.4 1.6-.8 1.7c-3.9.2-7.6-3.5-7.4-7.4z" fill="#fff"/></svg>
      SYDNEY: + 61 2 9000 5678
    </div>
    <nav class="nav" style="left:113px"><span class="active">Voices</span><span>Rates</span><span>Payments</span><span>News</span></nav>
    <div class="brand">Quorra Hub<i></i></div>
    <nav class="nav" style="left:740px"><span>About Us</span><span>Contact Us</span><span>Shortlist</span></nav>
  </header>
  <div class="ghost">QUORRA HUB</div>
  <h1 class="hero-title">AUSTRALIA'S TOP VOICES</h1>
  <div class="hero-sub">PROFESSIONAL CASTING</div>
  <div class="search"><span>SEARCH ARTIST</span><b><svg width="18" height="18" viewBox="0 0 18 18"><circle cx="7.5" cy="7.5" r="5.5" fill="none" stroke="#fff" stroke-width="2"/><path d="M11.5 11.5l4.5 4.5" stroke="#fff" stroke-width="2"/></svg></b></div>
  <svg class="chev" width="32" height="26" viewBox="0 0 32 26"><path d="M6 4l10 9 10-9M6 13l10 9 10-9" fill="none" stroke="#fff" stroke-width="2"/></svg>
</section>

<!-- FILTER -->
<form class="filter" aria-label="Find a voice">
  <div class="select" style="left:24px;top:25px">Location</div>
  <div class="select" style="left:265px;top:25px">Sex</div>
  <div class="select" style="left:507px;top:25px">Age range</div>
  <div class="select" style="left:24px;top:64px">Talent range</div>
  <div class="select" style="left:265px;top:64px">Language</div>
  <div class="select" style="left:507px;top:64px">Accent</div>
</form>
<div class="submit">SUBMIT NOW</div>

<!-- SPOTLIGHT -->
<section class="section spotlight">
  <div class="spot-glow" role="img" aria-label="Soft green and violet wave ribbons"></div>
  <div class="ghost">VOICE CAST</div>
  <h2 class="sec-title">Our Spotlight</h2>
  <span class="arrow left" style="left:111px;top:377px"></span>
  <article class="card featured" style="left:153px">
    <div class="photo" role="img" aria-label="Portrait of voice artist Lena Hartwell"></div>
    <h3>Lena Hartwell</h3><div class="role">Artist Auckland</div>
    <p>Lorem ipsum dolor sit amet, consectetur adipiscing elit</p>
  </article>
  <article class="card" style="left:386px">
    <div class="photo" role="img" aria-label="Portrait of voice artist TK Morrow"></div>
    <h3>TK Morrow</h3><div class="role">Artist Auckland</div>
    <p>Lorem ipsum dolor sit amet, consectetur adipiscing elit</p>
  </article>
  <article class="card" style="left:618px">
    <div class="photo" role="img" aria-label="Portrait of voice artist Ivy Castellan"></div>
    <h3>Ivy Castellan</h3><div class="role">Artist Auckland</div>
    <p>Lorem ipsum dolor sit amet, consectetur adipiscing elit</p>
  </article>
  <article class="card" style="left:846px">
    <div class="photo" role="img" aria-label="Portrait of voice artist Ivy Castellan"></div>
    <h3>Ivy Castellan</h3><div class="role">Artist Auckland</div>
    <p>Lorem ipsum dolor sit amet, consectetur adipiscing elit</p>
  </article>
  <span class="arrow right" style="left:1077px;top:377px"></span>
  <a class="btn" style="left:532px;top:588px;width:162px;height:39px">View More</a>
</section>

<!-- ABOUT -->
<section class="section about">
  <div class="about-wave" role="img" aria-label="Teal and green sound-wave ribbons"></div>
  <div class="ghost">WHO WE ARE</div>
  <h2>ABOUT QUORRA HUB</h2>
  <p style="top:180px">Lorem ipsum dolor sit amet, consectetur adipiscing elit, sed do eiusmod tempor incididunt</p>
  <p style="top:247px">ut labore et dolore magna aliqua. Ut enim ad minim veniam ullamco ut labore et dolore magna aliqua. Ut enim ad minim veniam ullamco</p>
  <a class="btn" style="left:140px;top:358px;width:162px;height:40px">Learn More</a>
  <div class="ring" style="left:645px;top:28px;width:476px;height:476px"></div>
  <div class="ring" style="left:668px;top:51px;width:430px;height:430px;border-color:rgba(124,193,66,.35)"></div>
  <div class="about-photo" role="img" aria-label="Close-up of a studio microphone with warm bokeh lights"></div>
</section>

<!-- NEWS -->
<section class="section news">
  <div class="ghost">BLOG &amp; NEWS</div>
  <h2 class="sec-title"><span class="light">Latest</span> News</h2>
  <article class="news-main">
    <div class="photo" role="img" aria-label="Gold studio microphone on a stand"></div>
    <h3>New Vovice Alert from Owen Ashcombe</h3>
    <p>Lorem ipsum dolor sit amet, consectetur adipiscing elit, sed do eiusmod tempor incididunt ut labore et dolore magna aliqua.</p>
    <a class="btn" style="left:26px;top:333px;width:130px;height:30px;font-size:11px">Learn More</a>
  </article>
  <article class="news-side" style="top:194px">
    <div class="photo" role="img" aria-label="Microphone with pop filter in an acoustic booth" style="background:linear-gradient(135deg,#2b2f35,#111418)"></div>
    <div class="txt"><h3>New Voice Alert</h3><div class="by">Owen Ashcombe</div><p>Lorem ipsum dolor sit amet, consectetur adipiscing elit, sed do eiusmod</p></div>
    <a class="btn" style="left:230px;top:128px;width:128px;height:28px;font-size:11px">Learn More</a>
  </article>
  <article class="news-side" style="top:392px">
    <div class="photo" role="img" aria-label="Microphone against a blue audio waveform screen" style="background:linear-gradient(135deg,#1d5fa0,#0e1a2a)"></div>
    <div class="txt"><h3>New Voice Alert</h3><div class="by">Owen Ashcombe</div><p>Lorem ipsum dolor sit amet, consectetur adipiscing elit, sed do eiusmod</p></div>
    <a class="btn" style="left:230px;top:128px;width:128px;height:28px;font-size:11px">Learn More</a>
  </article>
</section>

<!-- REVIEWS -->
<section class="section reviews">
  <div class="reviews-wave" role="img" aria-label="Glowing multicolour sound-wave ribbons"></div>
  <div class="ghost">REVIEWS</div>
  <h2 class="sec-title"><span class="light">What People</span> Says</h2>
  <span class="arrow left" style="left:110px;top:383px"></span>
  <div class="bubble" style="left:149px;top:225px;width:302px;height:302px;padding-top:50px">
    <div class="q">&ldquo;</div>
    <p>Morbi diam mauris viverra in gravida eu mattis in ante Morbi eget arcu Morbi porta libero id ullamcorper nonummy nibh ligula pulvinar metus eget consectetuer augue nisi quis lacus Ut ac mi quis lacu</p>
    <div class="who">Marcus Reid</div><div class="loc">Cty Location</div>
  </div>
  <div class="bubble" style="left:749px;top:225px;width:302px;height:302px;padding-top:50px">
    <div class="q">&ldquo;</div>
    <p>Morbi diam mauris viverra in gravida eu mattis in ante Morbi eget arcu Morbi porta libero id ullamcorper nonummy nibh ligula pulvinar metus eget consectetuer augue nisi quis lacus Ut ac mi quis lacu</p>
    <div class="who">Marcus Reid</div><div class="loc">Cty Location</div>
  </div>
  <div class="bubble main" style="left:421px;top:222px;width:360px;height:360px;padding-top:58px">
    <div class="q">&ldquo;</div>
    <p>Morbi diam mauris viverra in gravida eu mattis in ante Morbi eget arcu Morbi porta libero id ullamcorper nonummy nibh ligula pulvinar metus eget consectetuer augue nisi quis lacus</p>
    <div class="cite"><i></i><div><b>Paper Kite Studio</b><small>Nina Ford</small></div></div>
  </div>
  <span class="arrow right" style="left:1078px;top:383px"></span>
</section>

<!-- CLIENTS -->
<section class="section clients">
  <div class="ghost">CLIENTS</div>
  <h2 class="sec-title">Our <em>Clients</em></h2>
  <div class="client-box"></div>
  <div class="client" style="left:86px;top:281px">Ridgeway</div>
  <div class="client" style="left:268px;top:281px;color:#2c3e5a">Cocoa Lane</div>
  <div class="client" style="left:440px;top:281px">Unity Home</div>
  <div class="client" style="left:598px;top:281px">Triad Motors</div>
  <div class="client" style="left:760px;top:281px">Archway Eats</div>
  <div class="client" style="left:918px;top:281px">ClearSight</div>
  <div class="client" style="left:84px;top:406px">Ninefold</div>
  <div class="client" style="left:268px;top:406px">Lumière</div>
  <div class="client" style="left:440px;top:406px">Wavelength FM</div>
  <div class="client" style="left:594px;top:406px">SciWave</div>
  <div class="client" style="left:754px;top:406px">Listenly</div>
  <div class="client" style="left:922px;top:406px">Playline</div>
  <div class="dots"><i></i><i></i><i></i></div>
</section>

<!-- FOOTER -->
<footer class="section footer">
  <div class="footer-wave" role="img" aria-label="Faint sound-wave pattern"></div>
  <div class="brand">Quorra Hub<i></i></div>
  <div class="tag">JUST SAY THE WORD</div>
  <div class="fcol" style="left:427px">
    <h4>Navigation</h4>
    <ul><li>Voices</li><li>Rates</li><li>Payments</li><li>News</li></ul>
  </div>
  <div class="fcol" style="left:637px">
    <h4>Resources</h4>
    <ul><li>Contact Us</li><li>About Us</li><li>Privacy Policy</li><li>Terms of Use</li></ul>
  </div>
  <div class="fcol" style="left:864px;width:260px">
    <h4>Contact Us</h4>
    <div class="contact-row"><svg width="16" height="22" viewBox="0 0 16 22"><path d="M8 1a7 7 0 017 7c0 5-7 13-7 13S1 13 1 8a7 7 0 017-7z" fill="#7cc142"/><circle cx="8" cy="8" r="2.6" fill="#1b2b40"/></svg><span>Suite 101, 45 Harbour St Coogee<br>NSW 2034 Australia</span></div>
    <div class="contact-row"><svg width="20" height="20" viewBox="0 0 20 20"><circle cx="10" cy="10" r="10" fill="#7cc142"/><path d="M7 5.5l1.6 2.4-1 1.2a6 6 0 003 3l1.2-1 2.4 1.6-.8 1.7c-3.9.2-7.6-3.5-7.4-7.4z" fill="#fff"/></svg><span>SYDNEY: + 61 2 9000 5678<br>MELBOURNE: + 61 3 9000 1234</span></div>
  </div>
</footer>
<div class="copy">© Copyright 2018 Quorra Hub Pty Limited. Privacy Policy | Sitemap</div>

</body>
</html>
```